"VelTra" - Ketamine Clinic - Save Minds and Heal Hearts!! -

I need a very nice modern happy brain themed warm website design for our cutting edge modern and caring ketamine IV infusion clinic that also offers talk therapy and telemedicine visits.
A great design using the color schemes in out logos (grey, white, purples and that need metallic fading colored effect in the logo).

```html
<!DOCTYPE html>
<html lang="en">
<head>
<meta charset="utf-8">
<title>VelTra – Ketamine Infusion Therapy</title>
<link rel="stylesheet" href="https://fonts.googleapis.com/css2?family=Poppins:wght@400;500;600;700&display=swap">
<style>
:root{
  --purple:#7c10e2;
  --purple-deep:#6a0fd0;
  --violet-text:#8a14dc;
  --blue:#1d7fd8;
  --cyan:#16c0e8;
  --lavender:#f0e7fc;
  --lavender-soft:#f4edfd;
  --mint:#e6f8fc;
  --ink:#1c1c28;
  --body:#33333d;
  --muted:#7a7a86;
  --white:#ffffff;
}
*{box-sizing:border-box;margin:0;padding:0}
html,body{width:1200px;height:5124px;overflow:hidden}
body{position:relative;font-family:"Poppins",sans-serif;color:var(--body);background:var(--white)}
.abs{position:absolute}
.btn{position:absolute;display:flex;align-items:center;justify-content:center;border-radius:30px;color:var(--white);font-size:13px;font-weight:500}
.btn-purple{background:var(--purple)}
.btn-cyan{background:var(--cyan)}
.h-purple{color:var(--violet-text);font-weight:600;line-height:1.25}
.para{font-size:12.5px;line-height:20.5px;color:var(--body)}
.placeholder{position:absolute;border-radius:4px}

/* hero */
.hero{position:absolute;left:0;top:0;width:1200px;height:730px}
.logo{position:absolute;display:flex;align-items:center;gap:10px;font-size:30px;font-weight:700;color:var(--purple)}
.logo .dot{width:26px;height:26px;border-radius:50%;background:var(--purple)}
.nav{position:absolute;font-size:13px;color:var(--ink)}
.nav span{position:absolute;white-space:nowrap}
.eyebrow{font-size:15px;color:var(--ink);letter-spacing:.2px}
.hero-title{font-size:40px;line-height:42px;font-weight:600;color:var(--violet-text)}

/* help band */
.help{position:absolute;left:0;top:1325px;width:1200px;height:410px;background:linear-gradient(100deg,#6614e6 0%,#4a52ea 55%,#12bde6 100%)}
.help-card{position:absolute;top:175px;width:256px;height:146px;background:var(--white);border:4px solid #3ee0f0;border-radius:8px;display:flex;flex-direction:column;align-items:center;justify-content:center;gap:12px;color:var(--purple);font-weight:600;font-size:16px}
.help-card .ico{width:52px;height:52px;border-radius:50%;background:linear-gradient(135deg,#b46cf0,#6a1ee0)}

/* steps */
.step{position:absolute;top:3075px;width:202px;height:225px;background:var(--lavender);border-radius:10px;display:flex;flex-direction:column;align-items:center;padding-top:42px;text-align:center;font-size:12.5px;line-height:15px;color:var(--ink)}
.step .ico{width:58px;height:58px;border-radius:12px;background:linear-gradient(135deg,#3a8ae8,#7c22e2);margin-bottom:20px}

/* blog */
.blog{position:absolute;left:0;top:3445px;width:1200px;height:735px;background:var(--mint)}
.card{position:absolute;top:167px;width:310px;height:470px;background:var(--white)}
.card .img{height:220px}
.card .meta{position:absolute;left:26px;top:250px;font-size:10px;color:var(--muted)}
.card .title{position:absolute;left:26px;top:272px;width:265px;font-size:15px;line-height:21px;color:var(--ink);font-weight:500}
.card .txt{position:absolute;left:26px;top:330px;width:265px;font-size:11px;line-height:19px;color:var(--muted)}
.card .more{position:absolute;left:26px;top:405px;width:132px;height:38px;border:1px solid #b9d2f3;display:flex;align-items:center;justify-content:center;gap:12px;font-size:10px;font-weight:600;color:var(--blue)}

/* contact */
.info{position:absolute;left:112px;display:flex;align-items:center;gap:16px;font-size:11px;line-height:15px;color:var(--ink)}
.info .circle{width:52px;height:52px;border-radius:50%;background:var(--purple);display:flex;align-items:center;justify-content:center;flex:none}
.form{position:absolute;left:488px;top:4280px;width:650px;height:540px;background:var(--lavender-soft);border-radius:30px}
.field{position:absolute;height:48px;border:1px solid #8a8a96;background:var(--lavender-soft);font-size:12px;color:var(--body);padding:14px 22px}

/* footer */
.footer{position:absolute;left:0;top:4900px;width:1200px;height:224px}
.fnav{position:absolute;top:100px;font-size:13px;color:var(--white)}
.social{position:absolute;top:94px;width:22px;height:22px;border-radius:50%;background:var(--white)}
</style>
</head>
<body>

<!-- HERO -->
<section class="hero">
  <svg class="abs" style="left:0;top:0" width="1200" height="730" viewBox="0 0 1200 730">
    <defs>
      <linearGradient id="heroBg" x1="0" y1="0" x2="0" y2="1">
        <stop offset="0" stop-color="#ede2fb"/><stop offset="1" stop-color="#f4eefd"/>
      </linearGradient>
    </defs>
    <path d="M0 0H1200V500C1120 505 1060 585 960 560C860 540 790 600 700 605C640 608 600 620 590 710C580 620 540 605 470 600C380 592 320 530 250 560C180 590 80 520 0 530Z" fill="url(#heroBg)"/>
    <path d="M0 530C80 520 180 590 250 560C320 530 380 592 470 600C540 605 580 620 590 710C600 620 640 608 700 605C790 600 860 540 960 560C1060 585 1120 505 1200 500" fill="none" stroke="#9b4ee8" stroke-width="2"/>
  </svg>

  <div class="logo" style="left:104px;top:62px"><span class="dot"></span>VelTra</div>

  <nav class="nav" style="left:0;top:71px">
    <span style="left:522px">HOME</span>
    <span style="left:584px">ABOUT US</span>
    <span style="left:675px">TREATMENTS</span>
    <span style="left:794px">CONTACT US</span>
  </nav>
  <a class="btn btn-purple" style="left:929px;top:55px;width:166px;height:50px">Talk with Us</a>

  <p class="abs eyebrow" style="left:105px;top:224px">KETAMINE INFUSION THERAPY</p>
  <h1 class="abs hero-title" style="left:105px;top:274px">Get Well. Live Free.<br>Be Happy.</h1>
  <a class="btn btn-purple" style="left:98px;top:388px;width:232px;height:46px">Request my consultation</a>

  <div class="placeholder" role="img" aria-label="Illustration of a calm woman meditating among soft clouds and floating flowers"
       style="left:510px;top:130px;width:505px;height:405px;background:linear-gradient(160deg,#b9c6f6 0%,#e2b6f0 50%,#f2a9c9 100%)"></div>
</section>

<!-- INTRO -->
<div class="abs" style="left:0;top:730px;width:1200px;height:595px;background:linear-gradient(180deg,#ffffff 0%,#f6f4fe 55%,#e6f8fc 100%)"></div>
<p class="abs" style="left:0;top:740px;width:1200px;text-align:center;font-size:15px;font-weight:600;color:var(--ink)">Discover How We are</p>
<h2 class="abs" style="left:0;top:770px;width:1200px;text-align:center;font-size:32px;font-weight:500;color:var(--blue)">Ketamin Infusion for Mood Disorders</h2>

<div class="placeholder" role="img" aria-label="Photo of a woman sitting peacefully by a lake at sunset"
     style="left:126px;top:888px;width:332px;height:342px;border-radius:0;background:linear-gradient(160deg,#f6e3b4,#d9c9a8 50%,#7f9fb8)"></div>
<div class="placeholder" role="img" aria-label="Photo of balanced stones with a green sprout in raked sand"
     style="left:378px;top:988px;width:164px;height:236px;border-radius:0;border:6px solid #fff;background:linear-gradient(180deg,#efeeea,#c8c6c0)"></div>

<h2 class="abs h-purple" style="left:584px;top:900px;font-size:26px">Welcome to&nbsp; VelTra.com</h2>
<p class="abs para" style="left:584px;top:948px;width:505px">Lorem ipsum dolor sit amet consectetur. Augue placerat molestie dui sit eget ac. Maecenas eget amet amet gravida malesuada aliquet. At at ornare porttitor enim at aliquam fringilla. Sem in erat quam dictum enim sed. Faucibus nunc nibh nibh malesuada dui diam eu sollicitudin. Elementum ipsum cursus id arcu. Enim sed egestas sapien quis euismod. Massa neque sed pulvinar ac nunc quam arcu. Varius ultrices mi adipiscing pretium est. Suspendisse erat vehicula in feugiat pellentesque tellus molestie elementum nunc. Sit adipiscing porta lectus egestas elementum feugiat enim nulla nisl. Massa id consequat velit morbi vel elementum quis et.<br>Suspendisse amet urna maecenas amet arcu nisl urna. Sed eleifend arcu tortor mauris dui nunc viverra. In nisi suspendisse pulvinar arcu eu potenti.</p>

<!-- HOW CAN WE HELP -->
<section class="help">
  <div class="placeholder" role="img" aria-label="Soft flower pattern decoration" style="left:0;top:0;width:260px;height:410px;border-radius:0;background:linear-gradient(90deg,rgba(140,60,255,.45),rgba(140,60,255,0))"></div>
  <div class="placeholder" role="img" aria-label="Soft flower pattern decoration" style="left:880px;top:0;width:320px;height:410px;border-radius:0;background:linear-gradient(270deg,rgba(80,210,255,.5),rgba(80,210,255,0))"></div>
  <h2 class="abs" style="left:0;top:92px;width:1200px;text-align:center;font-size:25px;font-weight:500;color:var(--white)">How Can We Help You?</h2>
  <div class="help-card" style="left:160px"><span class="ico" role="img" aria-label="Sad face icon"></span>Depression</div>
  <div class="help-card" style="left:468px"><span class="ico" role="img" aria-label="Anxious head icon"></span>Anxiety</div>
  <div class="help-card" style="left:778px;border-color:#fff"><span class="ico" role="img" aria-label="Head profile icon"></span>PTSD</div>
</section>

<!-- WHAT IS -->
<section class="abs" style="left:0;top:1735px;width:1200px;height:505px;background:var(--lavender-soft)">
  <h2 class="abs h-purple" style="left:105px;top:142px;font-size:26px;width:420px">What Is IV Ketamine Infusion Therapy?</h2>
  <p class="abs para" style="left:110px;top:230px;width:435px">The most common side effects usually only occur up to two hours after the infusion has been administered. To help ensure the safety of patients, there is a two-hour window of supervision at the clinic following the administration before patients can leave and head home. Although you may not experience any of these side effects, the most common side effects of ketamine infusion therapy include:</p>
  <div class="placeholder" role="img" aria-label="Illustration of a man in a head profile surrounded by white and blue flowers"
       style="left:605px;top:50px;width:465px;height:355px;border-radius:48% 52% 40% 45%;background:linear-gradient(135deg,#f4f2f8,#c9d2e6 55%,#5a84b8)"></div>
</section>

<!-- WHY CHOOSE -->
<section class="abs" style="left:0;top:2240px;width:1200px;height:442px;background:var(--white)">
  <div class="placeholder" role="img" aria-label="Illustration of a serene woman with flowers and plants blooming from her head"
       style="left:110px;top:68px;width:450px;height:374px;border-radius:50% 50% 0 0;background:linear-gradient(180deg,#f3b8d8 0%,#c9b1f0 40%,#4a62c8 100%)"></div>
  <h2 class="abs h-purple" style="left:615px;top:115px;font-size:30px;line-height:45px;width:420px">Why Choose IV Ketamin Infusion Therapy</h2>
  <p class="abs para" style="left:618px;top:228px;width:440px">The most common side effects usually only occur up to two hours after the infusion has been administered. To help ensure the safety of patients, there is a two-hour window of supervision at the clinic following the administration before patients can leave and head home. Although you may not experience any of these side effects, the most common side effects of ketamine infusion therapy include:</p>
</section>

<!-- BANNER -->
<section class="abs" style="left:0;top:2682px;width:1200px;height:228px;background:var(--purple)">
  <h2 class="abs" style="left:0;top:56px;width:1200px;text-align:center;font-size:25px;line-height:33px;font-weight:500;color:var(--white)">Regain your mental health with the help of an IV Ketamine<br>Infusion Clinic!</h2>
  <a class="btn btn-cyan" style="left:490px;top:140px;width:232px;height:48px">Request my consultation</a>
</section>

<!-- STEPS -->
<h2 class="abs h-purple" style="left:0;top:2992px;width:1200px;text-align:center;font-size:26px">Steps Toward Living the Life you’ve Always Wanted</h2>
<div class="step" style="left:166px"><span class="ico" role="img" aria-label="Calendar icon"></span>Schedule a free<br>consultation to learn<br>more about the benefits<br>of ketamine or NAD+.</div>
<div class="step" style="left:394px"><span class="ico" role="img" aria-label="Consultation icon"></span>Meet with our physician for<br>an exam to determine if<br>you’re an eligible<br>candidate.</div>
<div class="step" style="left:622px;top:3072px"><span class="ico" role="img" aria-label="Treatment icon"></span>Begin your treatment the<br>same day or schedule<br>your treatment for a later<br>date.</div>
<div class="step" style="left:850px;top:3072px;font-size:15px;line-height:20px"><span class="ico" role="img" aria-label="Smiling face icon" style="border-radius:50%"></span>Start feeling<br>better!</div>

<!-- BLOG -->
<section class="blog">
  <h2 class="abs" style="left:0;top:85px;width:1200px;text-align:center;font-size:25px;font-weight:500;color:var(--ink)">Latest Blog</h2>

  <article class="card" style="left:112px">
    <div class="img" role="img" aria-label="Photo of swirling orange and gold light" style="background:linear-gradient(135deg,#3a2a1e,#c87a2e 50%,#2a2430)"></div>
    <p class="meta">22 Oct, 2020 &nbsp;/&nbsp; 248 Comments</p>
    <h3 class="title">Duis magna risus, convallis vel purus eu, sollicitudin volutpat velit.</h3>
    <p class="txt">Maecenas blandit auctor tempor. Class aptent taciti sociosqu ad litora torquent per conubia nostra.</p>
    <a class="more">READ MORE <svg width="16" height="10" viewBox="0 0 16 10"><path d="M0 5H14M10 1L14 5L10 9" fill="none" stroke="#1d7fd8" stroke-width="1.5"/></svg></a>
  </article>

  <article class="card" style="left:446px">
    <div class="img" role="img" aria-label="Photo of a woman sitting on a beach at sunset" style="background:linear-gradient(180deg,#f3e3c2,#b8c2c6 60%,#8a9aa6)"></div>
    <p class="meta">8 Sep, 2020 &nbsp;/&nbsp; 248 Comments</p>
    <h3 class="title">Donec ut ex eu libero euismod dapibus id quis ipsum.</h3>
    <p class="txt">Phasellus non feugiat turpis, non gravida lorem. Nulla fermentum odio in dolor dapibus, ac eleifend lectus ullamcorper.</p>
    <a class="more">READ MORE <svg width="16" height="10" viewBox="0 0 16 10"><path d="M0 5H14M10 1L14 5L10 9" fill="none" stroke="#1d7fd8" stroke-width="1.5"/></svg></a>
  </article>

  <article class="card" style="left:780px">
    <div class="img" role="img" aria-label="Photo of a lifeguard tower on a misty beach" style="background:linear-gradient(180deg,#e8c2b2,#c9a89a 50%,#6e6660)"></div>
    <p class="meta">24 May, 2020 &nbsp;/&nbsp; 248 Comments</p>
    <h3 class="title">Maecenas congue cursus metus eget bibendum phasellus dign.</h3>
    <p class="txt">Praesent semper enim at lacus sagittis, non semper eros ullamcorper. Duis id elemtum nisl, eu tincidunt nisl.</p>
    <a class="more">READ MORE <svg width="16" height="10" viewBox="0 0 16 10"><path d="M0 5H14M10 1L14 5L10 9" fill="none" stroke="#1d7fd8" stroke-width="1.5"/></svg></a>
  </article>
</section>

<!-- CONTACT -->
<h2 class="abs h-purple" style="left:104px;top:4283px;font-size:27px;line-height:33px;width:360px">Learn More About This Innovative New Treatment Option</h2>
<p class="abs para" style="left:105px;top:4400px;width:320px;font-size:12px;line-height:20px">The most common side effects usually only occur up to two hours after the infusion has been administered. To help ensure the safety of patients, there is a two-hour window of supervision :</p>

<div class="info" style="top:4544px">
  <span class="circle"><svg width="20" height="14" viewBox="0 0 20 14"><rect x="1" y="1" width="18" height="12" rx="1" fill="none" stroke="#fff" stroke-width="1.5"/><path d="M1 1L10 8L19 1" fill="none" stroke="#fff" stroke-width="1.5"/></svg></span>
  <span>Email<br>hello@veltraclinic.com</span>
</div>
<div class="info" style="top:4619px">
  <span class="circle"><svg width="18" height="18" viewBox="0 0 24 24"><path d="M6.6 10.8a15 15 0 006.6 6.6l2.2-2.2a1 1 0 011-.25 11.4 11.4 0 003.6.57 1 1 0 011 1V20a1 1 0 01-1 1A17 17 0 013 4a1 1 0 011-1h3.5a1 1 0 011 1c0 1.25.2 2.45.57 3.57a1 1 0 01-.25 1z" fill="none" stroke="#fff" stroke-width="1.6"/></svg></span>
  <span>Call Us<br>(00) 987 604 215</span>
</div>
<div class="info" style="top:4694px">
  <span class="circle"><svg width="20" height="20" viewBox="0 0 20 20"><circle cx="10" cy="10" r="8" fill="none" stroke="#fff" stroke-width="1.6"/><path d="M10 5V10L13 12" fill="none" stroke="#fff" stroke-width="1.6"/></svg></span>
  <span>Mon - Sat 9.00 - 18.00<br>Sunday Closed</span>
</div>

<section class="form">
  <h2 class="abs" style="left:44px;top:70px;font-size:25px;font-weight:500;color:var(--ink)">Get in Touch</h2>
  <div class="field" style="left:44px;top:114px;width:264px">Your name*</div>
  <div class="field" style="left:340px;top:114px;width:282px">Email*</div>
  <div class="field" style="left:44px;top:190px;width:270px">Phone Number*</div>
  <div class="field" style="left:340px;top:190px;width:282px">City</div>
  <div class="field" style="left:44px;top:268px;width:574px;height:128px">Your Message</div>
  <a class="btn btn-purple" style="left:44px;top:420px;width:216px;height:48px">Submit Message</a>
</section>

<!-- FOOTER -->
<footer class="footer">
  <svg class="abs" style="left:0;top:0" width="1200" height="224" viewBox="0 0 1200 224">
    <defs>
      <linearGradient id="footBg" x1="0" y1="0" x2="1" y2="0">
        <stop offset="0" stop-color="#7010e6"/><stop offset=".55" stop-color="#4a4cea"/><stop offset="1" stop-color="#14bde6"/>
      </linearGradient>
    </defs>
    <path d="M0 65C300 45 420 32 600 32C780 32 900 45 1200 65V224H0Z" fill="url(#footBg)"/>
  </svg>
  <div class="abs" style="left:488px;top:-92px;width:224px;height:224px;border-radius:50%;background:#fff;border:2px solid #9b4ee8;display:flex;align-items:center;justify-content:center">
    <span class="logo" style="position:static;font-size:34px"><span class="dot"></span>VelTra</span>
  </div>
  <span class="fnav" style="left:105px">HOME</span>
  <span class="fnav" style="left:166px">ABOUT US</span>
  <span class="fnav" style="left:257px">TREATMENTS</span>
  <span class="fnav" style="left:376px">CONTACT US</span>
  <span class="social" style="left:946px"></span>
  <span class="social" style="left:986px"></span>
  <span class="social" style="left:1027px"></span>
</footer>

</body>
</html>
```